Complete Stationary Package for Harbor Chapel
Harbor Chapel -- The Believers of Redfield (under Harbor Chapel and smaller)
Complete Stationary Package for Harbor Chapel  - Religion and Spirituality
Creative Brief
Use specific fonts
new, vibrant, creative (please see comments below -- suprise and impress me!))
Bright & Fun-filled
Martin Delvaux
Pastor
418 W. Brinley Ave Longview, TX 75612
hcredfield@mailnest.example
harborredfield.example
I love this logo, the shape and the concept and the way the c and the t work together. However, I would like stationary designers to please use a much more creative font. Also, feel free to change, enhance the colors of the logo itself as you feel is best.
OPTION ONE Service Times Prayer Sunday 10 am Friday 7 pm Sunday 6 pm Youth Service Wednesday 7 pm Friday 8 pm OPTION TWO Harbor Chapel The Believers of Redfield www.harborredfield.example I would like to see both options if possible in order to help me decide which works best. Thanks!
kmrowell kmrowell
Please use avatars for all information such as phone, email, website, etc.
Designers: Thanks for your wonderful contributions! I have uploaded an another version of the same logo that may look a lot better against a solid background. It may be that one looks good on a white back ground, the other on a solid background. Please help me make this determination. Also, know that I am willing to provide extra compensation for extra effort. Thanks! Martin
Also, please show designs with at least a couple of different fonts. Thanks!
Clarification: The following information should read -- Services Sunday 10 am Sunday 6 pm Wednesday 7 pm Prayer Friday 7 pm Youth Service / Activities Friday 8 pm Thanks!
Thanks for the immediate response to this contest! We're off to a fantastic start! Please keep in mind that I'm looking for a complete stationary package -- folder, letterhead, envelopes, electronic signature, cd labels, etc.

```html
<!DOCTYPE html>
<html lang="en">
<head>
<meta charset="utf-8">
<title>Harbor Chapel – Business Cards</title>
<link rel="stylesheet" href="https://fonts.googleapis.com/css2?family=Cinzel:wght@600&family=Arimo:wght@400;700&display=swap">
<style>
  :root {
    --stage: #26272b;
    --card: #ffffff;
    --brand-blue: #1d5fb3;
    --deep-blue: #1246a0;
    --brand-orange: #f07a1a;
    --brand-green: #6bb33a;
    --ink: #3a3d44;
    --rule: #b9bec7;
  }
  * { box-sizing: border-box; margin: 0; padding: 0; }
  html, body { width: 1200px; height: 852px; overflow: hidden; }
  body { background: var(--stage); position: relative; font-family: "Arimo", Arial, sans-serif; color: var(--ink); }

  .card {
    position: absolute; width: 560px; height: 320px;
    background: var(--card); border-radius: 14px; overflow: hidden;
    box-shadow: 0 10px 30px rgba(0,0,0,.45);
  }
  .card--front { left: 70px; top: 90px; }
  .card--back { left: 570px; top: 440px; }

  .swoosh { position: absolute; left: 0; bottom: 0; width: 560px; height: 110px; }

  .brand-block { display: flex; flex-direction: column; align-items: center; text-align: center; }
  .brand__dot { width: 34px; height: 34px; border-radius: 50%; background: var(--brand-orange); margin-bottom: 6px; }
  .brand__name { font-family: "Cinzel", serif; font-weight: 600; font-size: 21px; color: var(--brand-blue); white-space: nowrap; letter-spacing: .3px; line-height: 1.15; }
  .brand__tagline { font-size: 7px; letter-spacing: .7px; text-transform: uppercase; color: var(--brand-green); margin-top: 3px; font-weight: 700; white-space: nowrap; }

  .person__name { font-family: "Cinzel", serif; font-weight: 600; font-size: 17px; color: var(--brand-blue); }
  .person__role { font-family: "Cinzel", serif; font-weight: 600; font-size: 11px; color: var(--brand-blue); margin-top: 2px; }
  .person__address { font-size: 11px; line-height: 1.45; margin-top: 10px; }

  .contacts { list-style: none; font-size: 11px; }
  .contacts li { display: flex; align-items: center; gap: 7px; height: 17px; }
  .contacts svg { width: 11px; height: 11px; fill: var(--deep-blue); flex: none; }

  .divider { position: absolute; width: 1px; background: var(--rule); }

  /* front card */
  .card--front .brand-block { position: absolute; left: 14px; width: 230px; top: 92px; }
  .card--front .divider { left: 258px; top: 26px; height: 190px; }
  .card--front .details { position: absolute; left: 282px; top: 30px; }
  .card--front .contacts { margin-top: 14px; }

  /* back card */
  .card--back .brand-block { position: absolute; left: 0; width: 560px; top: 20px; }
  .card--back .person { position: absolute; right: 302px; top: 124px; text-align: right; }
  .card--back .divider { left: 276px; top: 120px; height: 92px; }
  .card--back .contacts { position: absolute; left: 294px; top: 122px; }
</style>
</head>
<body>

<svg width="0" height="0" style="position:absolute" aria-hidden="true">
  <defs>
    <symbol id="icon-phone" viewBox="0 0 24 24"><path d="M6.6 10.8a15.1 15.1 0 0 0 6.6 6.6l2.2-2.2a1 1 0 0 1 1-.25 11.4 11.4 0 0 0 3.6.57 1 1 0 0 1 1 1V20a1 1 0 0 1-1 1A17 17 0 0 1 3 4a1 1 0 0 1 1-1h3.5a1 1 0 0 1 1 1 11.4 11.4 0 0 0 .57 3.6 1 1 0 0 1-.25 1z"/></symbol>
    <symbol id="icon-mobile" viewBox="0 0 24 24"><path d="M7 1h10a2 2 0 0 1 2 2v18a2 2 0 0 1-2 2H7a2 2 0 0 1-2-2V3a2 2 0 0 1 2-2zm0 3v14h10V4zm5 15.2a1.2 1.2 0 1 0 0 2.4 1.2 1.2 0 0 0 0-2.4z"/></symbol>
    <symbol id="icon-fax" viewBox="0 0 24 24"><path d="M6 2h12v6H6zM3 9h18a1 1 0 0 1 1 1v8h-4v4H6v-4H2v-8a1 1 0 0 1 1-1zm5 7v4h8v-4z"/></symbol>
    <symbol id="icon-mail" viewBox="0 0 24 24"><path d="M2 5h20v14H2zm2 2v.6l8 5.2 8-5.2V7zm0 3v7h16v-7l-8 5.2z"/></symbol>
    <symbol id="icon-web" viewBox="0 0 24 24"><path d="M12 2a10 10 0 1 0 0 20 10 10 0 0 0 0-20zm6.9 6h-3a15 15 0 0 0-1.3-3.9A8 8 0 0 1 18.9 8zM12 4a13 13 0 0 1 1.9 4h-3.8A13 13 0 0 1 12 4zM4.3 14a8 8 0 0 1 0-4h3.4a16 16 0 0 0 0 4zm.8 2h3a15 15 0 0 0 1.3 3.9A8 8 0 0 1 5.1 16zm3-8h-3a8 8 0 0 1 4.3-3.9A15 15 0 0 0 8.1 8zM12 20a13 13 0 0 1-1.9-4h3.8A13 13 0 0 1 12 20zm2.3-6H9.7a14 14 0 0 1 0-4h4.6a14 14 0 0 1 0 4zm.3 5.9a15 15 0 0 0 1.3-3.9h3a8 8 0 0 1-4.3 3.9zm1.7-5.9a16 16 0 0 0 0-4h3.4a8 8 0 0 1 0 4z"/></symbol>
    <symbol id="swoosh" viewBox="0 0 560 110" preserveAspectRatio="none">
      <path d="M0 92 Q300 80 560 24 L560 110 L0 110 Z" fill="#1246a0"/>
      <path d="M0 96 Q300 88 560 40 L560 110 L0 110 Z" fill="#1d5fb3"/>
      <path d="M0 84 Q300 70 560 10 L560 20 Q300 78 0 90 Z" fill="#f07a1a"/>
      <path d="M0 80 Q300 64 560 2 L560 5 Q300 68 0 82 Z" fill="#c9ced6"/>
    </symbol>
  </defs>
</svg>

<article class="card card--front">
  <div class="brand-block">
    <span class="brand__dot"></span>
    <span class="brand__name">Harbor Chapel</span>
    <span class="brand__tagline">The Believers of Redfield</span>
  </div>
  <span class="divider"></span>
  <div class="details">
    <div class="person__name">Martin Delvaux</div>
    <div class="person__role">Pastor</div>
    <div class="person__address">418 W. Brinley Ave<br>Longview, TX 75612</div>
    <ul class="contacts">
      <li><svg><use href="#icon-phone"/></svg>555-201-4410</li>
      <li><svg><use href="#icon-mobile"/></svg>555-201-7725</li>
      <li><svg><use href="#icon-fax"/></svg>555-201-4412</li>
      <li><svg><use href="#icon-mail"/></svg>hcredfield@mailnest.example</li>
      <li><svg><use href="#icon-web"/></svg>www.harborredfield.example</li>
    </ul>
  </div>
  <svg class="swoosh" aria-hidden="true"><use href="#swoosh"/></svg>
</article>

<article class="card card--back">
  <div class="brand-block">
    <span class="brand__dot"></span>
    <span class="brand__name">Harbor Chapel</span>
    <span class="brand__tagline">The Believers of Redfield</span>
  </div>
  <div class="person">
    <div class="person__name">Martin Delvaux</div>
    <div class="person__role">Pastor</div>
    <div class="person__address">418 W. Brinley Ave<br>Longview, TX 75612</div>
  </div>
  <span class="divider"></span>
  <ul class="contacts">
    <li><svg><use href="#icon-phone"/></svg>555-201-4410</li>
    <li><svg><use href="#icon-mobile"/></svg>555-201-7725</li>
    <li><svg><use href="#icon-fax"/></svg>555-201-4412</li>
    <li><svg><use href="#icon-mail"/></svg>hcredfield@mailnest.example</li>
  </ul>
  <svg class="swoosh" aria-hidden="true"><use href="#swoosh"/></svg>
</article>

</body>
</html>
```